Its time for a new website

We are at a point now where we are in desperate need of a new website. It was last updated 2006 but still looks like its 1995. We are looking for something eye catching to our clients but easy to navigate and add/remove photos of jobs/trucks and information. Our key business is the manufacture of fire appliances and resale of parts and equipment.

www.dunmorerescue.com.au

Coding

Coded - Design and coding required

Number of Pages Required

5+ page

Requirements
Must have
• Logo

```html
<!DOCTYPE html>
<html lang="en">
<head>
<meta charset="utf-8">
<title>Dunmore Rescue – General Purpose Appliances / Rescue</title>
<link href="https://fonts.googleapis.com/css2?family=Open+Sans:wght@400;600&display=swap" rel="stylesheet">
<style>
:root{
  --red:#d0141b;
  --red-dark:#a80d12;
  --blue:#1e88d6;
  --brand-blue:#1f5fae;
  --text:#333;
  --muted:#7a7a7a;
  --line:#e6e6e6;
  --footer:#3a3a3a;
  --footer-text:#c8c8c8;
}
*{box-sizing:border-box;margin:0;padding:0}
html,body{width:1046px;height:1200px;overflow:hidden;background:#fff}
body{font-family:"Open Sans",sans-serif;color:var(--text);position:relative}
.header{position:absolute;left:0;top:0;width:1046px;height:96px}
.brand{position:absolute;left:86px;top:24px;display:flex;align-items:center;gap:8px}
.brand-dot{width:34px;height:34px;border-radius:50%;background:var(--red)}
.brand-name{font-size:17px;font-weight:600;color:var(--brand-blue)}
.contact-bar{position:absolute;right:86px;top:15px;display:flex;gap:26px;font-size:10px;color:var(--muted)}
.contact-bar span{display:flex;align-items:center;gap:4px}
.search{position:absolute;left:762px;top:56px;width:198px;height:26px;display:flex}
.search-field{flex:1;background:#f1f1f1;border:1px solid #e0e0e0;font-size:9px;font-style:italic;color:#aaa;padding:6px 4px}
.search-btn{width:34px;background:#5b5b5b;display:flex;align-items:center;justify-content:center}
.nav{position:absolute;left:0;top:96px;width:1046px;height:38px;background:linear-gradient(#e3141c,#b30c11);display:flex;padding-left:86px}
.nav a{position:relative;display:flex;align-items:center;height:38px;padding:0 18px;color:#fff;text-decoration:none;font-size:11px;font-weight:600}
.nav a+a::before{content:"";position:absolute;left:-4px;top:0;height:38px;width:1px;background:rgba(0,0,0,.25);transform:skewX(20deg)}
.nav a.active{background:var(--blue)}
.page-title{position:absolute;top:170px;width:1046px;text-align:center;font-size:18px;color:#333}
.product{position:absolute;left:0;width:1046px}
.product-photo{position:absolute;left:86px;width:392px;box-shadow:0 14px 12px -8px rgba(0,0,0,.3)}
.product-body{position:absolute;left:500px;width:450px}
.product-body h2{font-size:14px;font-weight:600;color:#333;margin-bottom:14px}
.product-body p{font-size:11px;line-height:18px;color:#444}
.btn{position:absolute;left:2px;width:110px;height:38px;background:var(--red);color:#fff;font-size:14px;font-weight:600;display:flex;align-items:center;justify-content:center}
.divider{position:absolute;left:0;width:1046px;height:1px;background:var(--line)}
.footer{position:absolute;left:0;top:1100px;width:1046px;height:100px;background:var(--footer)}
.footer-nav{position:absolute;left:86px;top:25px;font-size:9.5px;color:var(--footer-text)}
.footer-nav span{margin:0 6px}
.copyright{position:absolute;left:86px;top:52px;font-size:9.5px;color:#999}
.social{position:absolute;left:884px;top:27px;display:grid;grid-template-columns:repeat(3,23px);gap:4px}
.social i{display:block;width:23px;height:23px}
.counter{position:absolute;left:980px;top:50px;font-size:9.5px;color:var(--footer-text)}
</style>
</head>
<body>
<header class="header">
  <div class="brand"><div class="brand-dot"></div><span class="brand-name">Dunmore Rescue</span></div>
  <div class="contact-bar">
    <span><svg width="8" height="11" viewBox="0 0 8 11"><path d="M4 0a4 4 0 0 0-4 4c0 3 4 7 4 7s4-4 4-7a4 4 0 0 0-4-4zm0 5.5A1.5 1.5 0 1 1 4 2.5a1.5 1.5 0 0 1 0 3z" fill="#1e88d6"/></svg>Lot 14 Carrow Road Dunmore 6400 Western Australia</span>
    <span><svg width="10" height="10" viewBox="0 0 10 10"><path d="M2 0l2 2.5-1.2 1.3a6 6 0 0 0 3.4 3.4L7.5 6 10 8l-1.5 2C4 10 0 6 0 1.5z" fill="#1e88d6"/></svg>08 95550174</span>
    <span><svg width="11" height="11" viewBox="0 0 11 11"><rect x="0" y="3" width="11" height="8" rx="1" fill="#1e88d6"/><rect x="2" y="0" width="7" height="4" fill="#1e88d6"/><rect x="3" y="6" width="5" height="3" fill="#fff"/></svg>08 95550160</span>
    <span><svg width="9" height="10" viewBox="0 0 9 10"><circle cx="4.5" cy="2.5" r="2.5" fill="#1e88d6"/><path d="M0 10a4.5 4.5 0 0 1 9 0z" fill="#1e88d6"/></svg>Sigin in</span>
  </div>
  <div class="search">
    <div class="search-field">Search</div>
    <div class="search-btn"><svg width="14" height="14" viewBox="0 0 14 14"><circle cx="6" cy="6" r="4.5" stroke="#fff" stroke-width="2" fill="none"/><path d="M9.5 9.5L13 13" stroke="#fff" stroke-width="2.5"/></svg></div>
  </div>
</header>

<nav class="nav">
  <a>HOME</a><a>ABOUT US</a><a>PUMPERS</a><a>TANKERS</a><a class="active">GPA/RESCUE</a><a>LIGHT TANKERS</a><a>TRAILERS</a><a>SLIP-ON UNITS</a><a>CONTACT US</a>
</nav>

<h1 class="page-title">General Purpose Appliances / Rescue</h1>

<section class="product" style="top:0">
  <div class="product-photo" style="top:261px;height:230px;background:linear-gradient(135deg,#c8232a,#b9bfc4 60%,#6d6d6d)" role="img" aria-label="Red crewcab general purpose fire and rescue appliance"></div>
  <div class="product-body" style="top:260px">
    <h2>GPA in a Crewcab with Torrent / Velt pumpset</h2>
    <p>Well suited for road rescue, mines and smaller communities, these GPA's have everything. Available on Kaizu, Meridan or Harlo in 4x4 or 4x2 with single or Crewcab options available (Depending on chassis).<br>Features such as Pump and Roll capability, Foam production, Rescue equipment, live hoser-eels, suction hoses, large locker space, plenty of water and medium pump capacities of your choice to fulfill your requirements.<br><br>(Shown here) Kaizu based GPA in a Crewcab with Torrent / Velt pumpset.</p>
    <div class="btn" style="top:190px">READ MORE</div>
  </div>
</section>
<div class="divider" style="top:538px"></div>

<section class="product">
  <div class="product-photo" style="top:585px;height:180px;background:linear-gradient(180deg,#7f8f6a,#d9dde0 40%,#a9adb0)" role="img" aria-label="White single cab emergency response appliance"></div>
  <div class="product-body" style="top:583px">
    <h2>GVM Cabchassis, this single cab appliance</h2>
    <p>Pictured (Left) is a Versatile and Affordable solution for your General Purpose requirements. Based on a 6 tonne GVM Cabchassis, this single cab appliance is perfect for mines and road rescue with large locker volumes and various pump options available. Pump and Roll capability, Foam production, Rescue equipment, live hosereels, ulfill your requirements.</p>
    <div class="btn" style="top:142px">READ MORE</div>
  </div>
</section>
<div class="divider" style="top:817px"></div>

<section class="product">
  <div class="product-photo" style="top:862px;height:181px;background:linear-gradient(180deg,#8a7a5a,#e8e2dc 40%,#9c8a78)" role="img" aria-label="White four wheel drive light rescue appliance"></div>
  <div class="product-body" style="top:862px">
    <h2>Wheel drive version Based on Kaizu's KR300</h2>
    <p>A 4 Wheel drive version Based on Kaizu's KR300 makes an affordable go anywhere appliance available to you with many of the features found on it's larger brothers.<br>Pump and Roll capability, Foam production, Rescue equipment, live hosereels, suction hoses, large locker space, plenty of water and medium pump.</p>
    <div class="btn" style="top:142px">READ MORE</div>
  </div>
</section>

<footer class="footer">
  <div class="footer-nav">HOME<span>/</span>ABOUT US<span>/</span>PUMPERS<span>/</span>TANKERS<span>/</span>GPA/RESCUE<span>/</span>LIGHT TANKERS<span>/</span>TRAILERS<span>/</span>SLIP-ON UNITS<span>/</span>CONTACT US<span>/</span>NEW FOR 2006</div>
  <div class="copyright">©2015 dunmorerescue | All rights reserved 2015.</div>
  <div class="social">
    <i style="background:#3d8fd1"></i><i style="background:#3b5b9a"></i><i style="background:#5cb83c"></i>
    <i style="background:#ef6c1d"></i><i style="background:#7b5fb5"></i><i style="background:#3cb4c9"></i>
  </div>
  <div class="counter">C 19</div>
</footer>
</body>
</html>
```